Upmarket Bathroom and Kitchen ware supplier needs a classy business card design

We are a company based in Fiji, we sell plumbing ware (Kitchen and bathroom taps, Basins,showers, toilets etc) through up market show rooms to individuals and directly through Architects and designers of resorts and holiday houses for new builds and renovations. we are wanting to upgrade our over all look and brand. we are starting with a new logo but will be rebranding the whole business. This project is for a business card design for my management and tales team I would like it to be dark, classy and interesting

Target Market(s)

Resort directors and Management, High end holiday home owners

Contact Information for Business Card

Gavin Threlkeld
Director
+64219473518

Colors

Designer to choose colors to be used in the design.

Requirements
Must have
• Must have an upmarket appearance I like darker charcoal shades but will be guided by the designers
• Please any catch phrases like "Crafting remarkable living rooms" this belongs tpo one of our suppliers so can not be used.
Nice to have
• Double sided, so front dedicated to logo provided and back info about the business and the person.

```html
<!DOCTYPE html>
<html lang="en">
<head>
<meta charset="utf-8">
<title>Larkmoor Interiors – Business Card</title>
<link rel="stylesheet" href="https://fonts.googleapis.com/css2?family=Lato:wght@300;400;700&display=swap">
<style>
  :root {
    --backdrop: #8f8f8f;
    --card: #1b1b1c;
    --card-edge: #111112;
    --emboss: #2a2a2b;
    --accent: #b0182a;
    --ink-light: #e8e8e8;
    --ink-muted: #cfcfcf;
  }
  * { box-sizing: border-box; margin: 0; padding: 0; }
  html, body {
    width: 1171px; height: 1200px; overflow: hidden;
    background: var(--backdrop);
    font-family: "Lato", sans-serif;
  }
  .sheet {
    width: 1171px; height: 1200px;
    display: flex; flex-direction: column; align-items: center; justify-content: center;
    gap: 80px;
  }
  .card {
    width: 840px; height: 480px;
    background: var(--card);
    border: 1px solid var(--card-edge);
    position: relative;
    box-shadow: 0 18px 40px rgba(0,0,0,0.35);
  }
  /* Front */
  .card--front { display: flex; align-items: center; justify-content: center; }
  .brand {
    display: flex; align-items: center; gap: 22px;
  }
  .brand__dot {
    width: 58px; height: 58px; border-radius: 50%;
  }
  .brand__name {
    font-weight: 300; font-size: 40px; letter-spacing: 0.42em; line-height: 1;
    text-transform: uppercase; white-space: nowrap;
  }
  .card--front .brand__dot { background: var(--emboss); }
  .card--front .brand__name { color: var(--emboss); }

  /* Back */
  .card--back { display: flex; align-items: center; padding: 0 60px 0 70px; }
  .card--back .brand { flex: 1; gap: 18px; }
  .card--back .brand__dot { width: 44px; height: 44px; background: var(--accent); }
  .card--back .brand__name { color: var(--ink-light); font-size: 25px; letter-spacing: 0.36em; }
  .divider {
    width: 2px; height: 190px; background: var(--accent); margin: 0 34px 0 20px;
  }
  .contact { color: var(--ink-light); }
  .contact__name {
    color: var(--accent); font-weight: 700; font-size: 30px; letter-spacing: 0.01em;
    text-transform: uppercase; line-height: 1.1;
  }
  .contact__role { font-size: 17px; color: var(--ink-muted); margin: 6px 0 18px; }
  .contact__list { list-style: none; }
  .contact__item {
    display: flex; align-items: center; gap: 14px;
    font-size: 18px; line-height: 1.65; color: var(--ink-muted);
  }
  .contact__icon { width: 14px; height: 14px; flex: none; }
  .contact__icon * { fill: var(--accent); }
</style>
</head>
<body>
  <main class="sheet">
    <section class="card card--front" aria-label="Card front">
      <div class="brand">
        <span class="brand__dot"></span>
        <span class="brand__name">Larkmoor Interiors</span>
      </div>
    </section>

    <section class="card card--back" aria-label="Card back">
      <div class="brand">
        <span class="brand__dot"></span>
        <span class="brand__name">Larkmoor Interiors</span>
      </div>
      <span class="divider"></span>
      <div class="contact">
        <h1 class="contact__name">Marcus Hale</h1>
        <p class="contact__role">President</p>
        <ul class="contact__list">
          <li class="contact__item">
            <svg class="contact__icon" viewBox="0 0 16 16" aria-hidden="true"><path d="M3.2 1l2.6 3.2-1.6 1.8c1 2.2 3.4 4.6 5.8 5.8l1.8-1.6L15 12.8 13 15C6.6 14.6 1.4 9.4 1 3z"/></svg>
            +3120 4418 506
          </li>
          <li class="contact__item">
            <svg class="contact__icon" viewBox="0 0 16 16" aria-hidden="true"><path d="M1 3h14v10H1zM2.5 4.5v.6L8 9l5.5-3.9v-.6z"/></svg>
            info@larkmoor.com
          </li>
          <li class="contact__item">
            <svg class="contact__icon" viewBox="0 0 16 16" aria-hidden="true"><circle cx="8" cy="8" r="7"/></svg>
            www.larkmoor.com
          </li>
        </ul>
      </div>
    </section>
  </main>
</body>
</html>
```